Australia's newest tech recruitment startup

We are a new tech startup in the recruitment space.

We leverage the existing infrastructure of the recruitment network and bundle a value market based business model (like pixel flock) that appeals to business.

We are very individual, afraid of no one, minimalist, and defiantly NO "BS"!!

We're not cut price think Vellmar Auste rather than Korvani
Updates

Hey Everyone,

thanks so much for your designs. I have eliminated a lot of designs but if I havent to yours then your in with a shot. I would like to see the designs updated with a spot for our twitter handle, my blog address & our linkedIn group address. 

For some designs I think some of the above would look ok on the back of the card so not to make the front look too messy. 

thanks   

Target Market(s)

Our target market is SME's young baby boomer and Gen X

Industry/Entity Type

Business

Requirements
Must have
• Company logo, doesn't have to be both

```html
<!DOCTYPE html>
<html lang="en">
<head>
<meta charset="utf-8">
<title>Linkwell Hire – Business Card</title>
<link rel="stylesheet" href="https://fonts.googleapis.com/css2?family=Open+Sans:wght@400;600&family=Yellowtail&display=swap">
<style>
  :root {
    --stage: #3b3d40;
    --brand-blue: #1fa9dc;
    --brand-blue-deep: #1797c6;
    --card-white: #ffffff;
    --ink: #3a3a3a;
    --card-shadow: rgba(0, 0, 0, 0.35);
  }
  * { box-sizing: border-box; margin: 0; padding: 0; }
  html, body {
    width: 1200px;
    height: 900px;
    overflow: hidden;
    background: var(--stage);
  }
  .canvas {
    width: 1200px;
    height: 900px;
    display: flex;
    align-items: center;
    justify-content: center;
    gap: 60px;
  }
  .card {
    width: 520px;
    height: 297px;
    border-radius: 3px;
    box-shadow: 0 14px 30px var(--card-shadow);
    position: relative;
    overflow: hidden;
  }

  /* Front: blue logo side */
  .card--front {
    background: linear-gradient(160deg, var(--brand-blue) 0%, var(--brand-blue-deep) 100%);
    display: flex;
    align-items: center;
    justify-content: center;
  }
  .brand {
    display: flex;
    align-items: center;
    gap: 12px;
    font-family: "Open Sans", sans-serif;
    font-weight: 600;
    letter-spacing: 0.5px;
  }
  .brand__dot {
    width: 14px;
    height: 14px;
    border-radius: 50%;
  }
  .card--front .brand {
    color: var(--card-white);
    font-size: 46px;
  }
  .card--front .brand__dot { background: var(--card-white); }

  /* Back: contact side */
  .card--back {
    background: var(--card-white);
    padding: 30px 34px;
    font-family: "Open Sans", sans-serif;
    color: var(--ink);
  }
  .contact__name {
    font-family: "Yellowtail", cursive;
    font-weight: 400;
    font-size: 34px;
    line-height: 1;
    color: var(--brand-blue);
  }
  .contact__role {
    font-size: 12px;
    margin-top: 4px;
  }
  .contact__address {
    font-style: normal;
    font-size: 11px;
    line-height: 1.55;
    margin-top: 18px;
  }
  .contact__lines {
    list-style: none;
    font-size: 11px;
    line-height: 1.55;
    margin-top: 16px;
  }
  .contact__label {
    font-family: "Yellowtail", cursive;
    color: var(--brand-blue);
    font-size: 13px;
    margin-right: 6px;
  }
  .card--back .brand {
    position: absolute;
    right: 34px;
    bottom: 40px;
    color: var(--brand-blue);
    font-size: 30px;
    gap: 9px;
  }
  .card--back .brand__dot {
    width: 10px;
    height: 10px;
    background: var(--brand-blue);
  }
</style>
</head>
<body>
<main class="canvas">
  <section class="card card--front" aria-label="Card front">
    <div class="brand">
      <span class="brand__dot"></span>
      <span class="brand__name">Linkwell Hire</span>
    </div>
  </section>

  <section class="card card--back" aria-label="Card back">
    <h1 class="contact__name">Marcus Delane</h1>
    <p class="contact__role">managing director</p>
    <address class="contact__address">
      Linkwell Hire<br>
      48 Harbour Lane<br>
      Easton, NSW 2041
    </address>
    <ul class="contact__lines">
      <li><span class="contact__label">phone:</span>555 014 22 86</li>
      <li><span class="contact__label">e-mail:</span>info@linkwellhire.com.au</li>
    </ul>
    <div class="brand">
      <span class="brand__dot"></span>
      <span class="brand__name">Linkwell Hire</span>
    </div>
  </section>
</main>
</body>
</html>
```